Business Card Design

We are a General Practice - Family medicine
We also have Allied Health professionals working within our team

Industry/Entity Type

Business

Contact Information for Business Card

Front of the card to display:

BRAMBLEWICK MEDICAL
PHONE 6348 2917

5/41 Fennimore Parade
Launceston Tasmania 7284

Back of the card to display:

My Appointments
Date:
Time:
With:

Please remember to phone us on 6348 2917 to cancel your appointment if you can't keep it.
A fee applied to missed appointments

```html
<!DOCTYPE html>
<html lang="en">
<head>
<meta charset="utf-8">
<title>Bramblewick Medical – Business Card</title>
<link rel="stylesheet" href="https://fonts.googleapis.com/css2?family=Open+Sans:wght@400;600;700;800&family=Raleway:wght@500&display=swap">
<style>
  :root {
    --sky: #29abe2;
    --sky-soft: #bfe6f7;
    --leaf-soft: #dff0c8;
    --ink-grey: #8a8f94;
    --card: #ffffff;
    --backdrop: #eceae6;
    --edge: #d9d9d9;
  }
  * { box-sizing: border-box; margin: 0; padding: 0; }
  html, body { width: 1200px; height: 898px; overflow: hidden; }
  body {
    background: var(--backdrop);
    font-family: "Open Sans", Arial, sans-serif;
    position: relative;
  }
  .card {
    position: absolute;
    top: 91px;
    width: 440px;
    height: 708px;
    background: var(--card);
    border-radius: 26px;
    border: 2px solid var(--edge);
    overflow: hidden;
  }
  .card--front { left: 120px; }
  .card--back { left: 641px; }

  .brand-dot {
    position: absolute;
    left: 50%;
    top: 48px;
    width: 92px;
    height: 92px;
    margin-left: -46px;
    border-radius: 50%;
    background: var(--sky-soft);
  }
  .brand-name {
    position: absolute;
    left: 0; right: 0;
    top: 182px;
    text-align: center;
    font-family: "Raleway", Arial, sans-serif;
    font-weight: 500;
    font-size: 42px;
    color: var(--sky);
    letter-spacing: -0.5px;
  }

  /* Front */
  .icon-badge {
    position: absolute;
    left: 50%;
    width: 76px;
    height: 76px;
    margin-left: -38px;
    border-radius: 50%;
    background: var(--sky);
    border: 4px solid var(--card);
    display: flex;
    align-items: center;
    justify-content: center;
    z-index: 2;
  }
  .icon-badge svg { width: 40px; height: 40px; }
  .icon-badge--phone { top: 272px; }
  .icon-badge--pin { top: 462px; }

  .info-band {
    position: absolute;
    left: 26px;
    right: 26px;
    background: var(--sky);
    border-radius: 10px;
    color: #fff;
    font-weight: 700;
    font-size: 31px;
    line-height: 1.4;
    padding-left: 22px;
    display: flex;
    flex-direction: column;
    justify-content: center;
  }
  .info-band--phone { top: 336px; height: 112px; }
  .info-band--address { top: 520px; height: 154px; font-size: 29px; padding-left: 16px; }

  /* Back */
  .tagline {
    position: absolute;
    left: 0; right: 0;
    top: 262px;
    text-align: center;
    font-size: 14px;
    letter-spacing: 4px;
    color: var(--ink-grey);
  }
  .ribbon {
    position: absolute;
    left: 56px;
    top: 318px;
    width: 328px;
    height: 56px;
  }
  .ribbon svg { position: absolute; inset: 0; width: 100%; height: 100%; }
  .ribbon-label {
    position: relative;
    display: block;
    text-align: center;
    line-height: 56px;
    color: #fff;
    font-size: 28px;
    font-weight: 600;
    letter-spacing: 1px;
  }
  .appointment-field {
    position: absolute;
    left: 44px;
    right: 22px;
    height: 40px;
    border-bottom: 2px solid var(--sky);
    color: var(--ink-grey);
    font-size: 20px;
    line-height: 40px;
  }
  .appointment-field--date { top: 398px; }
  .appointment-field--time { top: 468px; }
  .appointment-field--with { top: 538px; }

  .reminder {
    position: absolute;
    left: 0; right: 0;
    top: 596px;
    text-align: center;
    color: var(--sky);
    font-weight: 700;
    font-size: 15px;
    line-height: 1.5;
  }
  .reminder-phone { font-size: 22px; line-height: 1.3; }
  .reminder-fee { margin-top: 8px; }
</style>
</head>
<body>

  <section class="card card--front" aria-label="Business card front">
    <div class="brand-dot"></div>
    <div class="brand-name">Bramblewick Medical</div>

    <div class="icon-badge icon-badge--phone">
      <svg viewBox="0 0 24 24" aria-hidden="true">
        <path fill="#fff" d="M6.6 10.8c1.4 2.8 3.8 5.1 6.6 6.6l2.2-2.2c.3-.3.7-.4 1-.2 1.1.4 2.3.6 3.6.6.6 0 1 .4 1 1V20c0 .6-.4 1-1 1C10.6 21 3 13.4 3 4c0-.6.4-1 1-1h3.5c.6 0 1 .4 1 1 0 1.3.2 2.5.6 3.6.1.3 0 .7-.2 1l-2.3 2.2z"/>
      </svg>
    </div>
    <div class="info-band info-band--phone">
      <span>HEALTHCARE CENTRE</span>
      <span>6348 2917</span>
    </div>

    <div class="icon-badge icon-badge--pin">
      <svg viewBox="0 0 24 24" aria-hidden="true">
        <path fill="none" stroke="#fff" stroke-width="2" d="M12 21s-6-6.2-6-11a6 6 0 0 1 12 0c0 4.8-6 11-6 11z"/>
        <circle cx="12" cy="10" r="2.3" fill="none" stroke="#fff" stroke-width="2"/>
        <path fill="none" stroke="#fff" stroke-width="2" d="M4 21h16"/>
      </svg>
    </div>
    <div class="info-band info-band--address">
      <span>5/41 Fennimore Parade</span>
      <span>Launceston Tasmania 7284</span>
    </div>
  </section>

  <section class="card card--back" aria-label="Business card back">
    <div class="brand-dot"></div>
    <div class="brand-name">Bramblewick Medical</div>
    <div class="tagline">HEALTHCARE CENTRE</div>

    <div class="ribbon">
      <svg viewBox="0 0 328 56" preserveAspectRatio="none" aria-hidden="true">
        <polygon fill="var(--sky)" points="0,0 328,0 312,28 328,56 0,56 16,28"/>
      </svg>
      <span class="ribbon-label">APPOINTMENT</span>
    </div>

    <div class="appointment-field appointment-field--date">Date</div>
    <div class="appointment-field appointment-field--time">Time</div>
    <div class="appointment-field appointment-field--with">With</div>

    <div class="reminder">
      <p>Please remember to phone us on</p>
      <p class="reminder-phone">6348 2917</p>
      <p>to cancel your appointment if you can't keep it.</p>
      <p class="reminder-fee">A fee applied to missed appointments</p>
    </div>
  </section>

</body>
</html>
```